Reiki business card

Please see uploaded files. There is a word document on there explaining what is required and what the other uploaded files are for. I am after a soft, relaxing, warm welcoming feel to the card. Thank you.

Business

```html
<!DOCTYPE html>
<html lang="en">
<head>
<meta charset="UTF-8">
<title>Reiki for Kids &amp; Companions – Business Card</title>
<link rel="stylesheet" href="https://fonts.googleapis.com/css2?family=Lobster&family=Exo+2:wght@400&display=swap">
<style>
  :root {
    --page: #ffffff;
    --card-left: #3679c1;
    --card-right: #438ccc;
    --band-edge: #3d7fc4;
    --band-core: #3463ae;
    --ink: #ffffff;
  }
  html, body {
    margin: 0;
    padding: 0;
    width: 840px;
    height: 1200px;
    overflow: hidden;
    background: var(--page);
  }
  .sheet {
    position: relative;
    width: 840px;
    height: 1200px;
    font-family: "Exo 2", sans-serif;
    color: var(--ink);
  }
  .card {
    position: absolute;
    left: 0;
    width: 840px;
    background: linear-gradient(90deg, var(--card-left), var(--card-right));
  }
  .card--front { top: 86px; height: 479px; }
  .card--back  { top: 587px; height: 480px; }

  .script {
    font-family: "Lobster", cursive;
    font-weight: 400;
    margin: 0;
  }
  .business-name {
    position: absolute;
    right: 58px;
    top: 66px;
    width: 360px;
    font-size: 46px;
    line-height: 56px;
    text-align: center;
  }
  .artwork-note {
    position: absolute;
    left: 53px;
    top: 198px;
    margin: 0;
    font-size: 28px;
    line-height: 36px;
  }
  .contact-band {
    position: absolute;
    left: 0;
    right: 0;
    top: 375px;
    height: 104px;
    border-top: 2px solid rgba(255,255,255,0.85);
    background: linear-gradient(90deg, var(--band-edge) 0%, var(--band-core) 30%, var(--band-core) 70%, var(--band-edge) 100%);
  }
  .practitioner {
    position: absolute;
    right: 56px;
    top: 13px;
    font-size: 29px;
    line-height: 36px;
  }
  .phone {
    position: absolute;
    left: 524px;
    top: 48px;
    display: flex;
    align-items: center;
    gap: 12px;
    font-size: 31px;
    letter-spacing: 0.5px;
  }
  .tagline {
    position: absolute;
    left: 0;
    right: 0;
    top: 135px;
    font-size: 45px;
    line-height: 56px;
    text-align: center;
  }
  .email {
    position: absolute;
    left: 132px;
    top: 352px;
    display: flex;
    align-items: center;
    gap: 14px;
    font-size: 29px;
  }
  .icon { display: block; }
</style>
</head>
<body>
<div class="sheet">
  <section class="card card--front">
    <h1 class="script business-name">Reiki for Kids<br>&amp; Companions</h1>
    <p class="artwork-note">Silohette of tree<br>with silohette of child<br>and dog<br>underneath tree</p>
    <div class="contact-band">
      <div class="practitioner">Maren Holloway</div>
      <div class="phone">
        <svg class="icon" width="38" height="38" viewBox="0 0 38 38" aria-hidden="true">
          <circle cx="19" cy="19" r="19" fill="#ffffff"/>
          <path d="M13.2 9.5c.8-.5 1.8-.3 2.3.5l2 3.2c.4.7.3 1.6-.3 2.1l-1.5 1.3c1 2.3 2.8 4.3 5 5.5l1.4-1.4c.6-.6 1.5-.7 2.2-.2l3.1 2.1c.8.5 1 1.6.4 2.3l-1.6 2c-.8 1-2.2 1.4-3.4.9-5.4-2.1-9.7-6.6-11.6-12.1-.4-1.2 0-2.5 1-3.3z" fill="#3a78bf"/>
        </svg>
        <span>0400 128 964</span>
      </div>
    </div>
  </section>

  <section class="card card--back">
    <p class="script tagline">Reiki - relaxes, restores balance<br>&amp; promotes healing</p>
    <div class="email">
      <svg class="icon" width="42" height="42" viewBox="0 0 42 42" aria-hidden="true">
        <circle cx="21" cy="21" r="21" fill="#ffffff"/>
        <path d="M11 18l10-7 10 7v11H11z" fill="#3d80c4"/>
        <path d="M13 19l8 5 8-5v8H13z" fill="#ffffff"/>
      </svg>
      <span>reikiforkidsandcompanions@mailbox.com</span>
    </div>
  </section>
</div>
</body>
</html>
```